Need a sleek, professional business card design for a Web Development business

I need a unique business card designed for a web development company. It is also the parent company for any ventures I do, such as my ClipWave channel, startup ideas I have, etc. I am the single member of "Bright Harbor Code LLC." I will attach my basic logo here, so you will see the current color scheme and have the asset available. Thank you!

Target Market(s)

Startups, SMB's, Professionals

Industry/Entity Type

Business

Font styles to use
Other font styles liked:
• Lovello for headings is what I use, but not necessary.

Colors

Designer to choose colors to be used in the design.

Requirements
Nice to have
• Sleek is the word. Professional, modern, dark.
Should not have
• Any work from someone else's design. Lacking originality.

```html
<!DOCTYPE html>
<html lang="en">
<head>
<meta charset="utf-8">
<title>Bright Harbor Code LLC – Business Card</title>
<link rel="stylesheet" href="https://fonts.googleapis.com/css2?family=Lato:wght@400&family=Poiret+One&family=Josefin+Sans:wght@300&display=swap">
<style>
  :root {
    --page-bg: #2c2c2e;
    --card-bg: #232323;
    --text-light: #f2f2f2;
    --accent: #e0743f;
    --deco-warm: #3a2924;
    --deco-deep: #30241f;
  }
  html, body {
    margin: 0;
    padding: 0;
    width: 1200px;
    height: 1200px;
    overflow: hidden;
    background: var(--page-bg);
  }
  .card {
    position: absolute;
    left: 175px;
    top: 336px;
    width: 859px;
    height: 490px;
    background: var(--card-bg);
    overflow: hidden;
  }
  .card-decor {
    position: absolute;
    inset: 0;
    width: 859px;
    height: 490px;
  }
  .brand {
    position: absolute;
    left: 55px;
    top: 116px;
    display: flex;
    align-items: center;
    gap: 14px;
    font-family: "Lato", sans-serif;
    font-weight: 400;
    font-size: 24px;
    color: var(--accent);
    letter-spacing: 0.5px;
  }
  .brand-square {
    width: 26px;
    height: 26px;
    background: var(--accent);
    border-radius: 4px;
  }
  .contact {
    position: absolute;
    left: 55px;
    top: 294px;
    font-family: "Lato", sans-serif;
    font-weight: 400;
    font-size: 21px;
    line-height: 24px;
    color: var(--text-light);
    letter-spacing: 0.4px;
  }
  .contact p { margin: 0; }
  .contact .address { margin-bottom: 9px; }
  .contact .phone,
  .contact .email { margin-bottom: 7px; }
  .identity {
    position: absolute;
    right: 64px;
    top: 354px;
    text-align: right;
    color: var(--text-light);
  }
  .identity .person-name {
    margin: 0;
    font-family: "Poiret One", sans-serif;
    font-size: 30px;
    line-height: 36px;
    font-weight: 400;
    letter-spacing: 1.5px;
  }
  .identity .person-role {
    margin: 2px 0 0;
    font-family: "Josefin Sans", sans-serif;
    font-weight: 300;
    font-size: 23px;
    line-height: 28px;
    letter-spacing: 0.3px;
  }
</style>
</head>
<body>
  <section class="card">
    <svg class="card-decor" viewBox="0 0 859 490" aria-hidden="true">
      <defs>
        <linearGradient id="decorFill" x1="0" y1="0" x2="1" y2="1">
          <stop offset="0" stop-color="var(--deco-deep)"/>
          <stop offset="1" stop-color="var(--deco-warm)"/>
        </linearGradient>
      </defs>
      <circle class="decor-corner-large" cx="859" cy="0" r="345" fill="url(#decorFill)"/>
      <circle class="decor-corner-small" cx="0" cy="490" r="56" fill="url(#decorFill)"/>
    </svg>

    <div class="brand">
      <span class="brand-square"></span>
      <span class="brand-name">Bright Harbor Code LLC</span>
    </div>

    <div class="contact">
      <p class="address">48 Lantern Row<br>Harborview 2045</p>
      <p class="phone">000 4821 7390</p>
      <p class="email">hello@brightharbor.dev</p>
      <p class="web">www.brightharbor.dev</p>
    </div>

    <div class="identity">
      <h1 class="person-name">YOUR FULL NAME</h1>
      <p class="person-role">CHIEF EXECUTIVE</p>
    </div>
  </section>
</body>
</html>
```